Line drawing of office spaces for luxury travel agencies in Denver and Brooklyn

We are a high-end luxury travel agency with two office locations - one in the Cherry Creek district of Denver, the other in Brooklyn, NY. I am seeking line drawings of the external and internal spaces to use in marketing and advertising in promoting these office spaces. We describe ourselves as an avant-garde travel consultancy with a vintage twist. Our imaging is highly curated and intentionally designed. We are building a campaign to expand our team of travel agents and want to incorporate clean lines, luxurious tone, and refined images.

Target Market(s)

Luxury travel agents

Industry/Entity Type

Travel Industry

Requirements
Must have
• Line drawing
• Clean design representative of the offices
• Creativity and a concept that allows the viewer to imagine the office on their own
Nice to have
• If possible to somehow combine the logo and both offices, that would be great!
• Black and white
Should not have
• Anything appearing cheap or clip art-y
• The photos provided are for reference - please do not just put a filter on the photos!

```html
<!DOCTYPE html>
<html lang="la">
<head>
<meta charset="utf-8">
<title>Vantoro — Officia</title>
<link rel="stylesheet" href="https://fonts.googleapis.com/css2?family=Saira+Condensed:wght@600&family=Saira+Extra+Condensed:wght@200&family=Source+Sans+3:wght@400&display=swap">
<style>
  :root {
    --ink: #141414;
    --paper: #ffffff;
    --sketch-light: #f1f1f1;
    --sketch-dark: #dcdcdc;
  }
  * { margin: 0; padding: 0; box-sizing: border-box; }
  html, body { width: 1200px; height: 1000px; overflow: hidden; background: var(--paper); }
  .poster {
    position: relative;
    width: 1200px;
    height: 1000px;
    background: var(--paper);
    color: var(--ink);
    font-family: "Source Sans 3", "Myriad Pro", sans-serif;
  }
  .storefront-illustration {
    position: absolute;
    left: 170px;
    top: 69px;
    width: 450px;
    height: 364px;
    background: linear-gradient(160deg, var(--sketch-light), var(--sketch-dark));
  }
  .brand-mark {
    position: absolute;
    left: 652px;
    top: 191px;
    overflow: visible;
  }
  .brand-name {
    font-family: "Saira Extra Condensed", "Arial Narrow", sans-serif;
    font-weight: 200;
    font-size: 190px;
    fill: var(--ink);
  }
  .brand-rule {
    position: absolute;
    left: 621px;
    top: 399px;
  }
  .sections {
    position: absolute;
    left: 0;
    top: 489px;
    width: 1200px;
  }
  .section {
    position: relative;
    height: 149px;
  }
  .section-title {
    position: absolute;
    left: 230px;
    top: -22px;
    font-family: "Saira Condensed", "Arial Narrow", sans-serif;
    font-weight: 600;
    font-size: 28px;
    line-height: 34px;
    letter-spacing: 2px;
    text-transform: uppercase;
    transform: rotate(7deg);
    transform-origin: left top;
  }
  .section-title span { display: block; }
  .section-title .indent { padding-left: 22px; }
  .section-title .indent-wide { padding-left: 62px; }
  .section-body {
    position: absolute;
    left: 481px;
    top: 0;
    font-size: 18.5px;
    line-height: 26px;
    font-weight: 400;
    white-space: nowrap;
  }
</style>
</head>
<body>
<main class="poster">
  <div class="storefront-illustration" role="img" aria-label="Black line drawing of a corner storefront office with awning, large windows and glass door"></div>

  <svg class="brand-mark" width="360" height="150" viewBox="0 0 360 150" aria-label="Vantoro">
    <text class="brand-name" x="0" y="140" textLength="352" lengthAdjust="spacingAndGlyphs">VANTORO</text>
  </svg>
  <svg class="brand-rule" width="414" height="4" viewBox="0 0 414 4" aria-hidden="true">
    <line x1="0" y1="2" x2="414" y2="2" stroke="var(--ink)" stroke-width="1.5"/>
  </svg>

  <section class="sections">
    <article class="section">
      <h2 class="section-title"><span>Quot</span><span class="indent">Philosophia</span></h2>
      <p class="section-body">Lorem ipsum dolor sit amet, vel ex omnis commodo<br>electram. Ignota accusam cum ut, ei mel justo nemore<br>noluisse. Has at integre verterem disputationi. Quot<br>philosophia an vel. Ei usu eros mundi facete. Tempor<br>intellegam in usu.</p>
    </article>
    <article class="section">
      <h2 class="section-title"><span>Autem</span><span class="indent-wide">Virtute</span></h2>
      <p class="section-body">Mel cu quot accusam assueverit, usu id quod legimus. Cum<br>no iudico animal moderatius, vidit iuvaret pri ne. Equidem<br>dignissim elaboraret quo eu. Sed unum gloriatur ea. Quo<br>nemore referrentur at, quem accusamus te sea, et graeci<br>animal mea.</p>
    </article>
    <article class="section">
      <h2 class="section-title"><span>Equidem</span><span class="indent-wide">Dignissim</span></h2>
      <p class="section-body">Pri eu invidunt vituperatoribus, nam ex facer possit oblique,<br>stet esse saepe id eum. Autem virtute concludaturque ut<br>mei, illud scaevola ius te. Mei commodo referrentur ex, vim<br>quas ubique perfecto ne. Ex est magna novum quaestio, an<br>vix atqui nostro neglegentur, ne pri oporteat evertitur.<br>Euismod facilisis comprehensam mel ne.</p>
    </article>
  </section>
</main>
</body>
</html>
```